Card design for orthopaedic surgeons working as The Brindlewood Orthopaedic Centre

Business cards, letterhead

Colors

Designer to choose colors to be used in the design.

Requirements
Must have
• Late addition.
• Cards letterhead must have logos of
• Corvane Federated Institute of Surgeons
• Meridale Orthopaedic Society
Nice to have
• Back of card to have space for appointment time to be added by hand and some blank space for writing incidental other notes.

```html
<!DOCTYPE html>
<html lang="en">
<head>
<meta charset="utf-8">
<title>The Brindlewood Orthopaedic Centre – Business Cards</title>
<link href="https://fonts.googleapis.com/css2?family=Roboto:wght@300;400;500;700&display=swap" rel="stylesheet">
<style>
  :root {
    --navy: #032c47;
    --sky: #4aa3df;
    --paper: #ffffff;
    --ink: #1c2a36;
    --backdrop: #e7e9ec;
  }
  * { margin: 0; padding: 0; box-sizing: border-box; }
  html, body { width: 1200px; height: 675px; overflow: hidden; }
  body {
    background: var(--backdrop);
    font-family: "Roboto", Arial, sans-serif;
    position: relative;
  }
  .card {
    position: absolute;
    top: 189px;
    width: 520px;
    height: 297px;
    border-radius: 16px;
    overflow: hidden;
    box-shadow: 0 6px 18px rgba(0,0,0,0.18);
  }
  .card-back { left: 53px; background: var(--navy); }
  .card-front { left: 627px; background: var(--paper); }

  .wordmark {
    position: absolute;
    font-family: "Roboto", Arial, sans-serif;
    font-weight: 300;
    white-space: nowrap;
    color: var(--sky);
  }
  .card-back .wordmark {
    left: 0; right: 0; top: 134px;
    text-align: center;
    font-size: 25px;
  }
  .card-front .wordmark {
    left: 28px; top: 158px;
    font-size: 14.5px;
  }

  .divider {
    position: absolute;
    left: 290px; top: 40px;
    width: 1px; height: 150px;
    background: var(--sky);
  }
  .contact {
    position: absolute;
    left: 310px; top: 34px;
    color: var(--ink);
  }
  .contact .person { font-size: 16px; font-weight: 700; color: var(--sky); }
  .contact .role { font-size: 11.5px; font-weight: 500; color: var(--navy); margin-top: 1px; }
  .contact .address { font-size: 10.5px; line-height: 14px; margin-top: 10px; }
  .contact ul { list-style: none; margin-top: 8px; font-size: 10.5px; line-height: 15px; }
  .contact li { display: flex; align-items: center; gap: 6px; }
  .contact svg { width: 10px; height: 10px; fill: var(--sky); flex: none; }

  .wave { position: absolute; left: 0; top: 0; width: 520px; height: 297px; }
</style>
</head>
<body>
  <section class="card card-back" aria-label="Card back">
    <div class="wordmark">The Brindlewood Orthopaedic Centre</div>
  </section>

  <section class="card card-front" aria-label="Card front">
    <svg class="wave" viewBox="0 0 520 297" aria-hidden="true">
      <path d="M0 297 L0 277 C180 272 262 252 340 212 C410 176 452 160 520 152 L520 297 Z" fill="var(--sky)"/>
      <path d="M0 297 L0 284 C182 279 266 260 344 220 C414 184 456 169 520 162 L520 297 Z" fill="var(--paper)"/>
      <path d="M0 297 L0 287 C184 282 268 264 346 224 C416 188 458 173 520 166 L520 297 Z" fill="var(--navy)"/>
    </svg>

    <div class="wordmark">The Brindlewood Orthopaedic Centre</div>
    <div class="divider"></div>

    <div class="contact">
      <div class="person">Alden Marrow</div>
      <div class="role">President</div>
      <div class="address">48 Quillon Ridge Parkway<br>Suite 310, Harrowgate, NV 89512</div>
      <ul>
        <li><svg viewBox="0 0 24 24"><path d="M6.6 10.8a15.1 15.1 0 0 0 6.6 6.6l2.2-2.2a1 1 0 0 1 1-.25 11.4 11.4 0 0 0 3.6.57 1 1 0 0 1 1 1V20a1 1 0 0 1-1 1A17 17 0 0 1 3 4a1 1 0 0 1 1-1h3.5a1 1 0 0 1 1 1c0 1.25.2 2.45.57 3.57a1 1 0 0 1-.25 1z"/></svg>222 555 0148</li>
        <li><svg viewBox="0 0 24 24"><path d="M2 5h20v14H2z M2 5l10 8 10-8" fill="none" stroke="var(--sky)" stroke-width="2.5"/></svg>info@brindlewoodortho.com</li>
        <li><svg viewBox="0 0 24 24"><circle cx="12" cy="12" r="9" fill="none" stroke="var(--sky)" stroke-width="2.2"/><path d="M3 12h18M12 3c3 3 3 15 0 18M12 3c-3 3-3 15 0 18" fill="none" stroke="var(--sky)" stroke-width="1.8"/></svg>www.brindlewoodortho.com</li>
      </ul>
    </div>
  </section>
</body>
</html>
```